Church Lanterns Over Millbrook Gospel Booklet Design

We need a booklet designed that we will be printing to hand out in our community. Wording for each page will be provided and we need graphic design to produce the layouts in a format ready for print. Booklet will be 4.75" x 4.75" square and a total of 12 pages: 1 cover page front, 1 cover page back, 10 inside pages some of which will be full spread across 2 pages.

Target Market(s)

English speaking Westerners

Industry/Entity Type

Religious

Font styles to use
Serif

Colors
ffffff
85abd2
0292cd
33b8a4
5c5c5c

Requirements
Must have
• Minimalist design with clean look described in attached document
Nice to have
• Aesthetically pleasing graphics, crisp fonts, excellent turn around times
Should not have
• Effeminate design, busy look with too much graphic and text

```html
<!DOCTYPE html>
<html lang="en">
<head>
<meta charset="utf-8">
<title>Lanterns Over Millbrook – Gospel Booklet Spreads</title>
<link rel="stylesheet" href="https://fonts.googleapis.com/css2?family=Montserrat:wght@500;600&family=Open+Sans:ital,wght@0,300;0,400;0,600;1,400;1,600&display=swap">
<style>
  :root {
    --bg: #ffffff;
    --paper: #ffffff;
    --blue: #0a9fe0;
    --blue-deep: #0292cd;
    --navy: #2b3c9e;
    --ink: #222222;
    --grey: #5c5c5c;
    --light: #ffffff;
    --rule: rgba(255,255,255,0.55);
  }
  * { box-sizing: border-box; margin: 0; padding: 0; }
  html, body { width: 1200px; height: 1056px; overflow: hidden; background: var(--bg); }
  body { position: relative; font-family: "Open Sans", Arial, sans-serif; color: var(--ink); }

  .spread {
    position: absolute; width: 520px; height: 260px;
    background: var(--paper); overflow: hidden;
    box-shadow: 0 10px 24px rgba(0,0,0,0.18);
  }
  .spread::after {
    content: ""; position: absolute; left: 259px; top: 0; width: 2px; height: 100%;
    background: rgba(0,0,0,0.12);
  }
  .spread--cover    { left: 40px;  top: 50px; }
  .spread--alien    { left: 640px; top: 50px; }
  .spread--created  { left: 40px;  top: 398px; }
  .spread--saved    { left: 640px; top: 398px; }
  .spread--truths   { left: 40px;  top: 746px; }
  .spread--declare  { left: 640px; top: 746px; }

  .photo { position: absolute; }
  .panel { position: absolute; background: var(--blue); color: var(--light); text-align: center; }
  .verse { font-size: 5px; line-height: 1.4; color: var(--light); }
  .verse-rule { border-top: 0.6px solid var(--rule); margin: 8px auto 6px; width: 85%; }

  /* Cover */
  .cover-photo { inset: 0; background: linear-gradient(180deg, #3a3633 0%, #2a2624 45%, #7a5a3c 75%, #2a1d14 100%); }
  .cover-blurb { position: absolute; left: 30px; top: 28px; width: 190px; font-size: 4.2px; line-height: 1.5; color: rgba(255,255,255,0.8); text-align: center; }
  .cover-sign { position: absolute; left: 30px; top: 175px; color: var(--light); }
  .cover-sign b { font-family: "Montserrat", sans-serif; font-weight: 600; font-size: 8px; letter-spacing: 0.5px; }
  .cover-sign span { display: block; font-size: 4px; opacity: 0.8; margin-top: 2px; }
  .cover-title { position: absolute; left: 300px; top: 48px; color: var(--light); font-family: "Montserrat", sans-serif; }
  .cover-title small { display: block; font-size: 12px; font-weight: 500; letter-spacing: 1.5px; }
  .cover-title strong { display: block; font-size: 23px; font-weight: 600; letter-spacing: 1.5px; line-height: 1.1; }

  /* Alienation */
  .alien-panel { left: 0; top: 0; width: 140px; height: 260px; padding: 28px 14px; font-size: 7.2px; line-height: 1.6; font-weight: 300; }
  .alien-crowd { left: 140px; top: 0; width: 120px; height: 260px; background: linear-gradient(180deg, #1b2a4a 0%, #6d89b8 40%, #0e1626 100%); }
  .alien-pray { left: 260px; top: 0; width: 260px; height: 260px; background: linear-gradient(120deg, #c08a6a 0%, #e4c1a2 40%, #d8d2c8 100%); }
  .alien-box { left: 290px; top: 50px; width: 210px; height: 180px; padding: 22px 18px; font-size: 5.8px; line-height: 1.45; font-weight: 600; }

  /* Created */
  .created-cross { left: 0; top: 0; width: 260px; height: 260px; background: radial-gradient(circle at 45% 60%, #f6c777 0%, #b9743a 18%, #4c4d58 45%, #2b3140 100%); }
  .created-land { left: 260px; top: 14px; width: 240px; height: 230px; background: linear-gradient(180deg, #3b5fa2 0%, #e79a72 22%, #8ab0c9 35%, #5f7d3e 60%, #3f5a26 100%); }
  .created-box { left: 320px; top: 76px; width: 200px; height: 120px; padding: 20px 16px; font-size: 6px; line-height: 1.4; font-weight: 600; }

  /* Saved */
  .saved-photo { left: 28px; top: 32px; width: 480px; height: 215px; background: linear-gradient(90deg, #4b3f3b 0%, #6a574f 50%, #9b6f5e 75%, #5a3c34 100%); }
  .saved-tag { position: absolute; left: 0; top: 22px; width: 190px; height: 20px; background: var(--blue); color: var(--light); font-size: 6.2px; font-weight: 600; padding: 6px 12px; }
  .saved-text { position: absolute; left: 50px; top: 72px; width: 240px; color: var(--light); text-align: center; font-size: 7px; line-height: 1.55; font-weight: 300; }
  .saved-verse { position: absolute; left: 50px; top: 185px; width: 240px; color: var(--light); text-align: center; font-size: 5.4px; font-style: italic; line-height: 1.4; }
  .saved-verse::before { content: ""; display: block; width: 70%; margin: 0 auto 6px; border-top: 0.6px solid var(--rule); }

  /* Truths */
  .truths-leaves { left: 0; top: 0; width: 260px; height: 260px; background: linear-gradient(160deg, #6b5a4a 0%, #a6784e 50%, #4a3c30 100%); }
  .truths-panel { left: 40px; top: 0; width: 160px; height: 260px; padding: 44px 8px 0; }
  .truths-lead { font-size: 6.5px; line-height: 1.45; margin-bottom: 14px; }
  .truths-grid { display: grid; grid-template-columns: 1fr 1fr; border-top: 0.6px solid var(--rule); }
  .truths-cell { padding: 8px 3px; border-bottom: 0.6px solid var(--rule); }
  .truths-cell:nth-child(odd) { border-right: 0.6px solid var(--rule); }
  .truths-cell h3 { font-size: 4.6px; font-weight: 600; margin-bottom: 4px; line-height: 1.3; }
  .truths-cell p { font-size: 3.4px; line-height: 1.4; }
  .truths-hands { left: 260px; top: 0; width: 260px; height: 260px; background: linear-gradient(150deg, #d9a75e 0%, #7d6a58 45%, #3c4a5a 100%); }
  .truths-box { left: 320px; top: 22px; width: 190px; height: 230px; padding: 40px 20px; font-size: 7px; line-height: 1.45; font-weight: 300; }

  /* Declare */
  .declare-text { position: absolute; left: 30px; top: 30px; width: 205px; text-align: center; font-size: 7.2px; line-height: 1.65; font-weight: 600; color: var(--ink); }
  .declare-bible { left: 0; top: 150px; width: 150px; height: 110px; background: linear-gradient(135deg, #e4e2de 0%, #c9c5be 55%, #6a3a2c 100%); }
  .declare-page { position: absolute; left: 260px; top: 0; width: 260px; height: 260px; background: var(--navy); }
  .declare-frame { position: absolute; left: 28px; top: 55px; width: 204px; height: 140px; border: 0.8px solid var(--rule); color: var(--light); text-align: center; padding-top: 20px; }
  .declare-frame p { font-size: 7px; line-height: 1.5; }
  .declare-frame .lord { font-family: "Montserrat", sans-serif; font-size: 15px; font-weight: 500; margin: 2px 0 4px; }
  .declare-frame .saved { font-family: "Montserrat", sans-serif; font-size: 12px; font-weight: 500; margin-top: 6px; }
  .declare-ref { position: absolute; left: 96px; top: 189px; background: var(--light); color: var(--navy); font-size: 6px; font-weight: 600; padding: 2px 5px; }
</style>
</head>
<body>

<section class="spread spread--cover">
  <div class="photo cover-photo" role="img" aria-label="Photo of a worship hall with a crowd raising hands, warm stage light"></div>
  <p class="cover-blurb">Lorem ipsum dolor sit amet, consectetur adipiscing elit, sed do eiusmod tempor incididunt ut labore et dolore magna aliqua. Ut enim ad minim veniam, quis nostrud exercitation ullamco laboris nisi ut aliquip ex ea commodo consequat.</p>
  <div class="cover-sign"><b>Lorem ipsum</b><span>Lorem ipsum dolor sit amet consectetur</span></div>
  <h1 class="cover-title"><small>LANTERNS OVER</small><strong>MILLBROOK</strong></h1>
</section>

<section class="spread spread--alien">
  <div class="panel alien-panel">This alienation from God is evident in a myriad of ways including poverty, crime, conflict in our relationships, and our internal struggles. But worse, when we die, we must face the consequences for our rejection of God by spending eternity in hell - a lake of fire created by God as the place where our treason is brought to justice.</div>
  <div class="photo alien-crowd" role="img" aria-label="Photo of a crowd raising hands at a concert"></div>
  <div class="photo alien-pray" role="img" aria-label="Photo of a woman praying with folded hands"></div>
  <div class="panel alien-box">
    But God does not want you to pay for your own sins. God loves us so much he sent his only son to save us. Jesus Christ died on the cross to serve our sentence for our rebellion against God and rose again on the third day. Since Christ paid our full penalty, we can be completely forgiven and reconciled to God.
    <div class="verse-rule"></div>
    <p class="verse">"For God so loved the world that he sent his one and only son that whosoever believes in him will not perish but have eternal life."<br>(John 3:16)</p>
  </div>
</section>

<section class="spread spread--created">
  <div class="photo created-cross" role="img" aria-label="Photo of a cross on a mountain top at sunrise"></div>
  <div class="photo created-land" role="img" aria-label="Photo of green hills and a country road under a sunset sky"></div>
  <div class="panel created-box">
    God willingly created the universe, meaning he envisioned, designed, and made us.
    <p class="verse" style="margin-top:22px">"In the beginning God created the heavens and the earth." (Genesis 1:1)</p>
  </div>
</section>

<section class="spread spread--saved">
  <div class="photo saved-photo" role="img" aria-label="Photo of a young woman praying against a brick wall"></div>
  <div class="saved-tag">Here is what you must do to be saved:</div>
  <p class="saved-text">First, ask Jesus Christ to save you (since he is God, he can hear you). Acknowledge that God is the rightful authority of the universe and your life. Apologize to him for your rebellion against God. Ask Jesus Christ to come into your life as your Lord and Savior. This decision will immediately trigger his miracle of salvation in you. God now lives in you!</p>
  <p class="saved-verse">"If you confess with your mouth that Jesus is Lord and believe in your heart that God raised him from the dead, you will be saved." (Romans 10:9)</p>
</section>

<section class="spread spread--truths">
  <div class="photo truths-leaves" role="img" aria-label="Photo of autumn leaves falling around a person"></div>
  <div class="panel truths-panel">
    <p class="truths-lead">This reality establishes some foundational truths for all of us:</p>
    <div class="truths-grid">
      <div class="truths-cell"><h3>God loves us</h3><p>He did not have to create us; we are here because he chose to love us.</p></div>
      <div class="truths-cell"><h3>God is the proper authority in our lives</h3><p>He designed and made us, so he rightfully owns us.</p></div>
      <div class="truths-cell"><h3>God knows the purpose of our lives</h3><p>He designed and made us, he knows why we are here.</p></div>
      <div class="truths-cell"><h3>God's truth is the truth we need</h3><p>He designed and made us, he knows what it takes for life to go well.</p></div>
    </div>
  </div>
  <div class="photo truths-hands" role="img" aria-label="Photo of a hand raised toward warm golden light"></div>
  <div class="panel truths-box">
    <div class="verse-rule" style="margin-top:0"></div>
    But we, mankind, have all rejected God's authority in our lives. And because he rightfully owns us, our rebellion against God is a grave injustice; an act of treason for which we deserve to be cut off from God forever.
    <div class="verse-rule" style="margin-top:14px"></div>
    <p class="verse">"For the wages of sin is death..."<br>(Romans 6:23)</p>
  </div>
</section>

<section class="spread spread--declare">
  <div class="photo declare-bible" role="img" aria-label="Photo of an open Bible on a table"></div>
  <p class="declare-text">Next, God has given us the Bible and his church as the key tools for us to grow in our understanding of God and our personal relationship with him. So, it is essential you find a local church that believes the Bible is 100% true. Tell one of the pastors you are a brand new Christian and they will help you from there.</p>
  <div class="declare-page">
    <div class="declare-frame">
      <p>If you declare with your mouth,</p>
      <p class="lord">“JESUS IS LORD”</p>
      <p>and believe in your heart that God<br>raised him from the dead,</p>
      <p class="saved">YOU WILL BE SAVED</p>
    </div>
    <span class="declare-ref">Romans 10:9</span>
  </div>
</section>

</body>
</html>
```